Specialised investor in e-mobility and energy wants business card design

We need a business card design that fits our existing corporate design. <The look and feel must be 'sharp'/'clean', dynamic, communicate momentum, professionalism etc (as one would imagine from a firm in the financial sector). We like the idea of a reverse-side of the card that includes the logo, and the name and contact details on the other. We expect the deliverable to be whatever format might be required to be able to get cards printed directly by a service such as tandor press. Our website is www.orm.capital

```html
<!DOCTYPE html>
<html lang="en">
<head>
<meta charset="utf-8">
<title>ORM Capital – Business Card</title>
<link rel="stylesheet" href="https://fonts.googleapis.com/css2?family=Questrial&family=Montserrat:wght@700&display=swap">
<style>
  :root {
    --bg: #e4e4e4;
    --card-white: #f5f5f6;
    --forest: #2d4721;
    --leaf: #84ad46;
    --ink-grey: #5c5c5c;
    --white: #ffffff;
  }
  * { margin: 0; padding: 0; box-sizing: border-box; }
  html, body {
    width: 1200px; height: 1200px; overflow: hidden;
    background: var(--bg);
    font-family: "Questrial", "Century Gothic", sans-serif;
  }
  .canvas { position: relative; width: 1200px; height: 1200px; }

  .card {
    position: absolute; left: 262px; width: 686px; height: 392px;
    border-radius: 20px; overflow: hidden;
  }
  .card--front { top: 165px; background: var(--card-white); }
  .card--back { top: 653px; background: var(--forest); }

  .wordmark {
    position: absolute; white-space: nowrap;
    font-family: "Questrial", "Century Gothic", sans-serif;
    font-weight: 400; letter-spacing: 0.5px; line-height: 1;
  }
  .card--front .wordmark { right: 48px; top: 64px; font-size: 50px; color: var(--forest); }
  .card--back .wordmark {
    left: 50%; top: 50%; transform: translate(-50%, -50%);
    font-size: 62px; color: var(--white);
  }

  .accent-bar { position: absolute; left: 0; top: 188px; width: 21px; height: 163px; }

  .contact { position: absolute; left: 42px; top: 190px; color: var(--ink-grey); }
  .contact__name {
    font-family: "Montserrat", "Century Gothic", sans-serif; font-weight: 700;
    font-size: 22px; letter-spacing: 0.4px; color: var(--forest); line-height: 1.1;
  }
  .contact__role { font-size: 16px; margin-top: 2px; }
  .contact__location { font-size: 17px; margin-top: 16px; }
  .contact__line { display: flex; align-items: center; gap: 13px; font-size: 17px; margin-top: 6px; }
  .contact__line:first-of-type { margin-top: 10px; }
  .contact__line svg { width: 14px; height: 14px; fill: var(--forest); flex: none; }
  .contact__web {
    font-family: "Montserrat", "Century Gothic", sans-serif; font-weight: 700;
    font-size: 15px; color: var(--forest); margin-top: 14px;
  }
</style>
</head>
<body>
<div class="canvas">
  <section class="card card--front">
    <div class="wordmark">ORM Capital</div>

    <svg class="accent-bar" viewBox="0 0 21 163" preserveAspectRatio="none" aria-hidden="true">
      <rect x="0" y="0" width="21" height="163" fill="var(--forest)"/>
      <rect x="0" y="0" width="21" height="75" fill="var(--leaf)"/>
      <polygon points="0,30 0,48 21,100 21,82" fill="var(--card-white)"/>
    </svg>

    <div class="contact">
      <div class="contact__name">DANIEL HARTWELL</div>
      <div class="contact__role">Managing Director</div>
      <div class="contact__location">Geneva, Switzerland</div>
      <div class="contact__line">
        <svg viewBox="0 0 24 24" aria-hidden="true"><path d="M6.6 10.8a15.1 15.1 0 0 0 6.6 6.6l2.2-2.2c.3-.3.7-.4 1-.2 1.1.4 2.3.6 3.6.6.6 0 1 .4 1 1V20c0 .6-.4 1-1 1A17 17 0 0 1 3 4c0-.6.4-1 1-1h3.5c.6 0 1 .4 1 1 0 1.3.2 2.5.6 3.6.1.3 0 .7-.2 1z"/></svg>
        <span>+41 79 000 4821</span>
      </div>
      <div class="contact__line">
        <svg viewBox="0 0 24 24" aria-hidden="true"><path d="M2 5h20v14H2z M4 7v1l8 5 8-5V7l-8 5z" fill-rule="evenodd"/></svg>
        <span>daniel@orm.capital</span>
      </div>
      <div class="contact__web">www.orm.capital</div>
    </div>
  </section>

  <section class="card card--back">
    <div class="wordmark">ORM Capital</div>
  </section>
</div>
</body>
</html>
```